TK & LJ Shearing Pty Ltd

We already have an existing logo created by Lumen Guild however we have restructured to a company. We would like someone to add Pty Ltd to our business name please.

Colors

Designer to choose only greyscale colors for use in the design.

```html
<!DOCTYPE html>
<html lang="en">
<head>
<meta charset="utf-8">
<title>TK &amp; LJ Shearing Pty Ltd — Business Card</title>
<link rel="stylesheet" href="https://fonts.googleapis.com/css2?family=Crimson+Pro:wght@400;700&family=Open+Sans:wght@400&display=swap">
<style>
  :root {
    --backdrop: #8a8c8e;
    --card: #1c1c1c;
    --ink: #ffffff;
    --muted: #e6e6e6;
  }
  html, body {
    margin: 0;
    padding: 0;
    width: 1200px;
    height: 884px;
    overflow: hidden;
    background: var(--backdrop);
  }
  .canvas {
    position: relative;
    width: 1200px;
    height: 884px;
  }
  .card {
    position: absolute;
    left: 100px;
    top: 136px;
    width: 1000px;
    height: 612px;
    background: var(--card);
    color: var(--ink);
    box-shadow: 0 18px 40px rgba(0,0,0,0.35);
  }
  .brand {
    position: absolute;
    right: 80px;
    top: 70px;
    text-align: right;
    font-family: "Crimson Pro", serif;
    font-weight: 400;
    color: var(--ink);
    line-height: 0.95;
  }
  .brand-initials {
    display: block;
    font-size: 150px;
    letter-spacing: 2px;
  }
  .brand-trade {
    display: block;
    font-size: 72px;
    letter-spacing: 3px;
    margin-top: 6px;
  }
  .brand-entity {
    display: block;
    font-size: 52px;
    letter-spacing: 3px;
    margin-top: 4px;
  }
  .contact-name {
    position: absolute;
    left: 80px;
    top: 338px;
    display: flex;
    align-items: flex-end;
    gap: 16px;
    font-family: "Crimson Pro", serif;
    font-weight: 700;
    font-size: 46px;
    letter-spacing: 1px;
  }
  .contact-name .rule {
    width: 340px;
    height: 2px;
    background: var(--ink);
    margin-bottom: 10px;
  }
  .contact-list {
    position: absolute;
    left: 70px;
    top: 420px;
    margin: 0;
    padding: 0;
    list-style: none;
  }
  .contact-list li {
    display: flex;
    align-items: center;
    gap: 14px;
    height: 42px;
    color: var(--muted);
  }
  .contact-list svg {
    width: 20px;
    height: 20px;
    fill: var(--ink);
    flex: none;
  }
  .contact-serif {
    font-family: "Crimson Pro", serif;
    font-size: 28px;
    letter-spacing: 0.5px;
  }
  .contact-sans {
    font-family: "Open Sans", sans-serif;
    font-size: 26px;
  }
</style>
</head>
<body>
<main class="canvas">
  <section class="card" aria-label="TK &amp; LJ Shearing business card">
    <h1 class="brand">
      <span class="brand-initials">TK &amp; LJ</span>
      <span class="brand-trade">SHEARING</span>
      <span class="brand-entity">PTY LTD</span>
    </h1>

    <div class="contact-name">
      <span>NED</span>
      <span class="rule"></span>
    </div>

    <ul class="contact-list">
      <li>
        <svg viewBox="0 0 24 24" aria-hidden="true"><path d="M12 2a7 7 0 0 0-7 7c0 5 7 13 7 13s7-8 7-13a7 7 0 0 0-7-7zm0 9.5A2.5 2.5 0 1 1 12 6.5a2.5 2.5 0 0 1 0 5z"/></svg>
        <span class="contact-serif">PO Box 418 YARROWDALE WA 6350</span>
      </li>
      <li>
        <svg viewBox="0 0 24 24" aria-hidden="true"><path d="M6.6 10.8a15.1 15.1 0 0 0 6.6 6.6l2.2-2.2a1 1 0 0 1 1-.25 11.4 11.4 0 0 0 3.6.57 1 1 0 0 1 1 1V20a1 1 0 0 1-1 1A17 17 0 0 1 3 4a1 1 0 0 1 1-1h3.5a1 1 0 0 1 1 1c0 1.25.2 2.45.57 3.6a1 1 0 0 1-.25 1z"/></svg>
        <span class="contact-serif">044 5182907</span>
      </li>
      <li>
        <svg viewBox="0 0 24 24" aria-hidden="true"><path d="M2 5h20v14H2zm2 2v.4l8 5.2 8-5.2V7zm0 2.8V17h16V9.8l-8 5.2z"/></svg>
        <span class="contact-sans">tkljshearing@mailbox.com</span>
      </li>
    </ul>
  </section>
</main>
</body>
</html>
```